Brightwell Pixel - Design & Marketing Website Re-branding

UPDATE:
We are working on finalizing our color palette but are hoping that the designers will guide us to the right choice of colors by looking at our color inspiration file that we just uploaded and lead us in the right direction.

-----

I am exploring new design inspiration for a re-branding of my website. My current website is old and outdated and I lack the time to design it myself in addition to the fact that I am my own worst client.

I do website design, development and marketing as well as some SEO consulting and business development for small to mid-size companies in a range of industries.

https://brightwellpixel-example.com

I like clean modern designs without cartoon images. The brands I'm going after are looking for a professional look and feel. I need something that shows my many years of being in business that is very professional.

I prefer minimal use of color. Mostly black and white with maybe one or two other colors. I am open to the suggestions by the designer.

Target Market(s)

Small to mid-size companies

Industry/Entity Type

Website Design, SEO and Markeitng

Number of Pages Required

4 page

Font styles to use
Sans Serif

Requirements
Must have
• Must be clean, modern and professional - I am not a huge fan of a lot of color and I'm open to new color suggestions by the designer
Nice to have
• A good balance of whitespace to content and graphics
Should not have
• Please no people illustrations

```html
<!DOCTYPE html>
<html lang="en">
<head>
<meta charset="utf-8">
<title>Brightwell Pixel — Website Design &amp; Marketing</title>
<link rel="stylesheet" href="https://fonts.googleapis.com/css2?family=Inter:wght@400;500;600;700&display=swap">
<style>
:root{
  --ink:#0a0a0a;
  --ink-soft:#1b1b1b;
  --paper:#ffffff;
  --text:#3a3a3a;
  --muted:#555;
  --line:#8a8a8a;
  --chip:#eeeeee;
  --teal:#1d4a4a;
  --teal-glow:rgba(40,110,110,.35);
}
*{box-sizing:border-box;margin:0;padding:0}
html,body{width:1200px;height:2834px;overflow:hidden;background:var(--paper);font-family:"Inter",sans-serif;color:var(--text)}
section,header,footer{position:relative;width:1200px;overflow:hidden}
.abs{position:absolute}
.center{left:0;right:0;text-align:center}

/* hero */
.hero{height:619px;background:var(--ink);color:var(--paper)}
.wave{position:absolute;background:radial-gradient(ellipse at center,var(--teal-glow),rgba(10,10,10,0) 70%)}
.brand{font-weight:600;font-size:24px;letter-spacing:-.5px;color:var(--paper)}
.menu-icon{left:1086px;top:37px}
.pill{left:500px;top:148px;width:194px;height:25px;border-radius:13px;background:#2e2e2e;font-size:10px;font-weight:600;line-height:25px;text-align:center;letter-spacing:.2px}
.hero h1{top:176px;font-size:82px;font-weight:700;line-height:96px;letter-spacing:-1px}
.hero .lead{top:386px;font-size:17px}
.btn-light{background:var(--paper);color:#222;border-radius:4px;font-size:13px;display:flex;align-items:center;gap:8px;padding:0 10px}
.hero .what{left:479px;top:439px;height:33px}
.hero .chat{left:624px;top:439px;height:33px;display:flex;align-items:center;gap:10px;font-size:13px}

/* services */
.services{height:507px}
.services h2{top:672px;font-size:40px;font-weight:600;color:#333}
.svc{top:765px;width:333px;height:290px;border:1px solid #333;padding:22px 20px}
.svc svg{display:block;margin-bottom:22px}
.svc h3{font-size:24px;font-weight:400;color:#333;margin-bottom:14px}
.svc h3 b{font-weight:600}
.svc p{font-size:15px;line-height:27px;color:var(--muted)}
.chip{position:absolute;left:20px;bottom:20px;background:var(--chip);border-radius:3px;font-size:13px;padding:8px 7px;color:#333}

/* quote */
.quote{position:absolute;top:1126px;height:366px;background:var(--ink);color:var(--paper)}
.quote blockquote{position:absolute;left:300px;width:600px;top:52px;text-align:center;font-size:40px;font-weight:500;line-height:57px}
.quote cite{position:absolute;left:0;right:0;top:290px;text-align:center;font-style:normal;font-size:20px;font-weight:500}

/* about */
.about{position:absolute;top:1492px;height:598px}
.about h2{top:106px;font-size:42px;font-weight:400;color:#333}
.about h2 b{font-weight:700}
.about .intro{left:150px;width:900px;top:176px;font-size:17px;line-height:25px;text-align:center}
.value{top:333px;width:333px;height:157px;background:linear-gradient(180deg,#121212,#2a2a2a);color:var(--paper);padding:18px 20px}
.value h3{font-size:24px;font-weight:600;margin-bottom:14px}
.value p{font-size:15px;line-height:27px;color:#e5e5e5}

/* cta */
.cta{position:absolute;top:2090px;height:384px;background:var(--ink);color:var(--paper)}
.cta h2{left:82px;top:56px;font-size:104px;font-weight:600;letter-spacing:1px}
.cta p{left:83px;top:193px;font-size:17px}
.cta .get{left:1030px;top:248px;height:33px;font-size:14px}

/* clients */
.clients{position:absolute;top:2474px;height:176px;display:flex;align-items:center;justify-content:space-around;padding:0 70px}
.client{display:flex;align-items:center;gap:10px;font-size:26px;font-weight:600;color:#333}
.client i{display:inline-block;width:26px;height:26px;border-radius:50%;background:#555}

/* footer */
.site-footer{position:absolute;top:2650px;height:184px;background:var(--ink);color:var(--paper)}
.site-footer .brand{left:84px;top:30px}
.foot-links{right:84px;top:36px;display:flex;align-items:center;gap:18px;font-size:13px}
.social{width:17px;height:17px;border:1.6px solid var(--paper);border-radius:50%}
.rule{left:84px;right:84px;top:96px;height:1px;background:#3a3a3a}
.copy{left:84px;top:127px;font-size:13px}
.legal{right:84px;top:127px;font-size:13px;display:flex;gap:14px}
</style>
</head>
<body>

<header class="hero">
  <div class="wave" role="img" aria-label="Flowing teal line-wave background" style="left:300px;top:-80px;width:1000px;height:500px"></div>
  <div class="wave" role="img" aria-label="Flowing teal line-wave background" style="left:-200px;top:250px;width:1100px;height:420px"></div>
  <div class="abs brand" style="left:84px;top:40px">brightwellpixel.</div>
  <svg class="abs menu-icon" width="26" height="26" viewBox="0 0 26 26" fill="#e6e6e6" aria-label="Menu">
    <rect x="0" y="0" width="11" height="11"/><rect x="15" y="0" width="11" height="11"/>
    <rect x="0" y="15" width="11" height="11"/><rect x="15" y="15" width="11" height="11"/>
  </svg>
  <div class="abs pill">BRIGHTWELL PIXEL</div>
  <h1 class="abs center">Every business has a<br>story. We help you tell it.</h1>
  <p class="abs center lead">Compelling website experiences that elevate your business.</p>
  <div class="abs btn-light what">What We Do
    <svg width="12" height="8" viewBox="0 0 12 8"><path d="M1 1l5 5 5-5" fill="none" stroke="#222" stroke-width="2"/></svg>
  </div>
  <div class="abs chat">
    <svg width="17" height="15" viewBox="0 0 17 15" fill="none" stroke="#fff" stroke-width="1.5"><rect x="4" y="1" width="12" height="9"/><path d="M1 4v9h11"/></svg>
    Let’s chat
  </div>
</header>

<section class="services">
  <h2 class="abs center" style="top:53px">what we do.?</h2>
  <article class="abs svc" style="left:84px;top:146px">
    <svg width="44" height="38" viewBox="0 0 44 38" fill="none" stroke="#333" stroke-width="3"><rect x="2" y="2" width="40" height="34" rx="3"/><path d="M2 11h40"/><circle cx="8" cy="6.5" r="1" fill="#333"/><circle cx="13" cy="6.5" r="1" fill="#333"/><circle cx="18" cy="6.5" r="1" fill="#333"/></svg>
    <h3>Websites <b>Simplified</b></h3>
    <p>A Complete End-To-End Website Subscription Solution That Propels Your Business Forward.</p>
    <span class="chip">Website Solution</span>
  </article>
  <article class="abs svc" style="left:433px;top:146px">
    <svg width="46" height="44" viewBox="0 0 46 44" fill="none" stroke="#333" stroke-width="2.5"><path d="M30 3l13 13-6 6-13-13z"/><path d="M24 9L10 15 3 41l26-7 6-14"/><path d="M3 41l12-12"/><circle cx="18" cy="26" r="3"/></svg>
    <h3>Custom <b>Website Design</b></h3>
    <p>Blending The Best Principles Of Design, Data And Functionality To Express Your Brand.</p>
    <span class="chip">Design Services</span>
  </article>
  <article class="abs svc" style="left:783px;top:146px">
    <svg width="46" height="42" viewBox="0 0 46 42" fill="none" stroke="#333" stroke-width="3"><path d="M6 24v-4a17 17 0 0134 0v4"/><rect x="3" y="22" width="7" height="11" rx="2"/><rect x="36" y="22" width="7" height="11" rx="2"/><path d="M16 22a7 7 0 0114 0v4a7 7 0 01-14 0z"/><path d="M39 33c0 5-6 7-13 7"/></svg>
    <h3>Website <b>Support</b></h3>
    <p>Reliable Top Tier CMS Website Support, Maintenance And Hosting,</p>
    <span class="chip">Website Care</span>
  </article>
</section>

<section class="quote">
  <div class="wave" role="img" aria-label="Flowing teal line-wave accent" style="left:200px;top:180px;width:1100px;height:260px"></div>
  <div class="wave" role="img" aria-label="Faint dotted grid accent" style="left:-60px;top:-40px;width:420px;height:160px;opacity:.5"></div>
  <blockquote>Brightwell Pixel provided us with a high quality, functional, easy to navigate and beautiful website</blockquote>
  <cite>- j. reyes</cite>
</section>

<section class="about">
  <div class="wave" role="img" aria-label="Faint grey dotted grid accent" style="left:-40px;top:40px;width:420px;height:120px;background:radial-gradient(ellipse,rgba(0,0,0,.06),rgba(255,255,255,0) 70%)"></div>
  <div class="wave" role="img" aria-label="Faint grey line-wave accent" style="left:820px;top:460px;width:480px;height:180px;background:radial-gradient(ellipse,rgba(0,0,0,.07),rgba(255,255,255,0) 70%)"></div>
  <h2 class="abs center">we create <b>websites that inspire,.</b></h2>
  <p class="abs intro">we are a collaborative team of word nerds, choreographers of shapes &amp; ideas, ambassadors of data, content warriors and inspirational conversationalists ready to help you no matter where you are in your journey.<br>we have a deep understanding of what it takes to grow a business and we collaborate with you every step of the way from strategy to implementation and beyond.</p>
  <article class="abs value" style="left:84px"><h3>Proven Process</h3><p>We Have Carefully Crafted Each Step In Our Process For Successful Outcomes.</p></article>
  <article class="abs value" style="left:433px"><h3>Connection</h3><p>We Take The Time To Truly Listen And Understand Your Audience And Business Needs.</p></article>
  <article class="abs value" style="left:783px"><h3>Exceeding Your Goals</h3><p>We Develop Actionable Strategies For Success Based On Your Unique Goals.</p></article>
</section>

<section class="cta">
  <div class="wave" role="img" aria-label="Flowing teal line-wave accent" style="left:350px;top:180px;width:950px;height:260px"></div>
  <div class="wave" role="img" aria-label="Faint dotted grid accent" style="left:-60px;top:-30px;width:360px;height:140px;opacity:.5"></div>
  <h2 class="abs">Let’s work together</h2>
  <p class="abs">Start Your Project Now and get a free consultation</p>
  <div class="abs btn-light get">Get started</div>
</section>

<section class="clients" aria-label="Clients">
  <span class="client"><i></i>Fairpath Learning</span>
  <span class="client">Kova Ventures</span>
  <span class="client">Harlow Legal</span>
  <span class="client"><i></i>Keystone</span>
  <span class="client">Coastal Kitchen</span>
</section>

<footer class="site-footer">
  <div class="abs brand">brightwellpixel.</div>
  <div class="abs foot-links">
    <span style="margin-right:16px">Let’s chat</span>
    <span class="social" aria-label="Social link"></span>
    <span class="social" aria-label="Social link"></span>
    <span class="social" aria-label="Social link"></span>
  </div>
  <div class="abs rule"></div>
  <div class="abs copy">© 2024 Brightwell Pixel, LLC. All Rights Reserved.</div>
  <div class="abs legal"><span>Privacy.</span><span>Terms.</span><span>Disclaimer.</span></div>
</footer>

</body>
</html>
```